Verdane Clinical Spa needs an eye-catching poster to help promote our largest sale of spring!

We need a poster that will go on the back of the doors in the patient rooms. Our medical spa is professional and high-end, so we want the poster to look sophisticated, yet very eye-catching.
This project is for our Marigold Jubilee special, our second largest sale of the year.

Name: Marigold Jubilee
Slogan: Let Your Beauty Bloom
Sale: The More You Buy, The More You Save

Choose from your favorite spa services
NEVRIL, Laser Treatments, Microderms, and More!

It would be great to have something blooming. Flowers, or somehow make a woman look like she's blooming.

I am attaching a visual description of our special. However, the poster should NOT include the pricing tiers. I am also attaching our business logo. Thank you!!

Target Market(s)

A majority are women, but some are men. Around 25-55 in age. Middle to upper class who are likely to spend more money.

Industry/Entity Type

Medical

Font styles to use
Sans Serif
Script

Colors

Designer to choose colors to be used in the design.

Requirements
Must have
• Name of promotion: Marigold Jubilee
• Slogan: "Let Your Beauty Bloom"
• Concept "The more you buy, the more you save on your favorite spa services"
• Select from your favorite spa services such as NEVRIL, laser treatments, microderms, and more!
• Website: VerdaneSpaDeals.com
• Our logo (attached)
Nice to have
• Modern and creative design. Somehow tying in the "Let your beauty bloom" theme. We don't want the focus to be "The more you buy the more you save"
• We are looking for a unique design that is unlike traditional medical spas in the area that typically include a lot of white and a lot of overly photoshopped images.
• Creativity is key! Something that's different than just text and images. We would be so excited to see that!
Should not have
• Not too much text, but enough to get the point across.

```html
<!DOCTYPE html>
<html lang="en">
<head>
<meta charset="utf-8">
<title>Marigold Jubilee – Verdane Clinical Spa</title>
<link rel="stylesheet" href="https://fonts.googleapis.com/css2?family=Great+Vibes&family=Crimson+Pro:ital,wght@0,700;1,700&family=Alegreya+Sans:ital,wght@0,400;1,700&display=swap">
<style>
  :root {
    --page: #ffffff;
    --mint-band: #b4f7ae;
    --mint-top: #b9f5b3;
    --mint-bottom: #ffffff;
    --violet: #8b1ee3;
    --ink: #1a1a1a;
    --silhouette-top: #b9bfd0;
    --silhouette-bottom: #d9c4f0;
    --bloom: #e45fd6;
  }
  * { box-sizing: border-box; margin: 0; padding: 0; }
  html, body { width: 1200px; height: 1000px; overflow: hidden; background: var(--page); }
  .canvas { position: relative; width: 1200px; height: 1000px; }

  .poster {
    position: absolute; left: 297px; top: 97px; width: 618px; height: 796px;
    background: var(--mint-band);
  }
  .poster-field {
    position: absolute; left: 16px; top: 16px; right: 16px; bottom: 16px;
    background: linear-gradient(to bottom, var(--mint-top), var(--mint-bottom));
  }
  .poster-frame {
    position: absolute; left: 37px; top: 34px; width: 541px; height: 725px;
    border: 2px solid var(--violet);
  }

  .hero-art {
    position: absolute; left: 103px; top: 153px; width: 472px; height: 485px;
    border-radius: 60% 40% 0 50% / 40% 50% 0 60%;
    background: linear-gradient(to bottom, var(--silhouette-top), var(--silhouette-bottom));
    opacity: 0.75;
  }
  .bloom-accent {
    position: absolute; left: 460px; top: 88px; width: 64px; height: 64px;
    border-radius: 50%; background: var(--bloom);
  }

  .promo-title {
    position: absolute; left: 81px; top: 100px;
    font-family: "Great Vibes", cursive; font-weight: 400; font-size: 58px; line-height: 1;
    color: var(--violet); white-space: nowrap;
  }
  .slogan {
    position: absolute; left: 96px; top: 272px;
    font-family: "Crimson Pro", serif; font-style: italic; font-weight: 700;
    font-size: 40px; line-height: 1.1; color: var(--violet); white-space: nowrap;
  }
  .offer {
    position: absolute; left: 97px; top: 369px;
    font-family: "Alegreya Sans", sans-serif; font-size: 23px; line-height: 45px;
    letter-spacing: 1.3px; color: var(--ink); white-space: nowrap;
  }
  .services-label {
    position: absolute; left: 97px; top: 479px;
    font-family: "Alegreya Sans", sans-serif; font-style: italic; font-weight: 700;
    font-size: 26px; line-height: 30px; color: var(--violet); letter-spacing: 0.5px;
  }
  .services-label .colon { color: var(--ink); font-style: normal; font-weight: 400; }
  .services {
    position: absolute; left: 97px; top: 517px;
    font-family: "Alegreya Sans", sans-serif; font-size: 23px; line-height: 32px;
    letter-spacing: 1.3px; color: var(--ink); white-space: nowrap;
  }
  .website {
    position: absolute; left: 97px; top: 696px;
    font-family: "Crimson Pro", serif; font-weight: 700; font-size: 20px; line-height: 24px;
    letter-spacing: 0.5px; color: var(--ink); white-space: nowrap;
  }
  .brand {
    position: absolute; left: 318px; top: 668px;
    display: flex; align-items: center; gap: 8px;
  }
  .brand-dot { width: 18px; height: 18px; border-radius: 50%; background: var(--mint-band); }
  .brand-name {
    font-family: "Alegreya Sans", sans-serif; font-weight: 400; font-size: 22px; line-height: 28px;
    color: var(--ink); white-space: nowrap;
  }
</style>
</head>
<body>
<main class="canvas">
  <section class="poster">
    <div class="poster-field"></div>
    <div class="hero-art" role="img" aria-label="Illustration of a woman in profile with long flowing, swirling hair"></div>
    <div class="bloom-accent" role="img" aria-label="Pink blooming flower ornament"></div>
    <div class="poster-frame"></div>
    <h1 class="promo-title">Marigold Jubilee</h1>
    <p class="slogan">Let Your Beauty Bloom!</p>
    <p class="offer">The more you buy, the more you save<br>on your favorite spa services.</p>
    <p class="services-label">Select from<span class="colon">:</span></p>
    <p class="services">NEVRIL • laser treatments • microderms<br>and more!</p>
    <p class="website">VerdaneSpaDeals.com</p>
    <div class="brand">
      <span class="brand-dot"></span>
      <span class="brand-name">Verdane Clinical Spa</span>
    </div>
  </section>
</main>
</body>
</html>
```